Luxury and organic beauty products need a Design

We need a bottle and packaging design for a new business in New Zealand, called Kelvara Botanicals. We are creating a selection of Luxury and premium products to have at the Kelvara luxury villa's (www.kelvaraluxuryvilla.com), as well to sell online and at boutique stores.

The products are: Body wash, Shampoo, Conditioner, Hand wash, Body lotion, Air fresheners and Bath salts.

We would like to use the Kelvara Botanicals logo in Silver as Kelvara Luxury Villa's a having it in Gold, so it separates the two products. Also the packaging will be Navy Blue along with the silver.

The final design should be sleek, sophisticated and have a luxury feel. Our customers will have the product in the bathroom and kitchen so the bottles must be proud to show off. " This should look and feel like a very high end product.

Boxes will have embossed writing (logo) and a slightly textured feel or look.

Please find attached images of some examples to use for inspiration only.

Target Market(s)

Luxury boutique villas, Boutique stores, High end stores

Industry/Entity Type

Personal and hair care

Colors
0054AA
0677BA
7BADD7
CADEEF
E8F1F8
FFC000
F8CF3A
FAE287
FDF2CF
FEFAEE

Requirements
Must have
• Use the provided Logo, look and feel luxurious, but at the same time organic
Nice to have
• A bottle that reminds precious stones. I have just attached an example
Should not have
• Dark colour, heavy fonts

```html
<!DOCTYPE html>
<html lang="en">
<head>
<meta charset="utf-8">
<title>Kelvara Luxury Lodge – Bath Range Labels</title>
<link href="https://fonts.googleapis.com/css2?family=Open+Sans:wght@300;400&display=swap" rel="stylesheet">
<style>
  :root {
    --page: #f5f5f5;
    --label: #fbfbfa;
    --ink: #5f5f5f;
    --gold: #c99a1c;
    --cream: #f1e6c8;
    --swatch: #8f8f8f;
    --salt: #d7ecf5;
  }
  * { margin: 0; padding: 0; box-sizing: border-box; }
  html, body { width: 1200px; height: 969px; overflow: hidden; }
  body {
    background: var(--page);
    font-family: "Open Sans", sans-serif;
    color: var(--ink);
    position: relative;
  }
  .label {
    position: absolute;
    overflow: hidden;
    text-align: center;
    box-shadow: 0 2px 14px rgba(0,0,0,0.06);
  }
  .label > * { position: absolute; left: 0; right: 0; line-height: 1; font-weight: 400; }

  .label--conditioner { left: 94px; top: 100px; width: 280px; height: 600px; background: var(--label); }
  .label--bodywash { left: 470px; top: 180px; width: 310px; height: 660px; background: var(--label); }
  .label--salt {
    left: 891px; top: 530px; width: 186px; height: 316px; border-radius: 14px;
    background: linear-gradient(160deg, #e5f3f9, var(--salt));
  }

  .leaf-area {
    background: radial-gradient(ellipse at center, rgba(241,230,200,0.45), rgba(241,230,200,0.15) 60%, transparent 75%);
  }
  .label--conditioner .leaf-area { top: 430px; height: 150px; left: 10px; right: 10px; }
  .label--bodywash .leaf-area { top: 230px; height: 160px; left: 90px; right: 10px; }

  .brand-mark {
    margin: 0 auto;
    border-radius: 50%;
    border: 3px solid var(--gold);
  }
  .label--conditioner .brand-mark { top: 48px; width: 118px; height: 118px; }
  .label--bodywash .brand-mark { top: 40px; width: 120px; height: 120px; }
  .label--salt .brand-mark { top: 24px; width: 60px; height: 60px; border-width: 2px; border-color: var(--swatch); }

  .brand-name { color: var(--gold); letter-spacing: 0.1em; }
  .brand-sub { color: var(--gold); letter-spacing: 0.18em; }
  .label--conditioner .brand-name { top: 176px; font-size: 34px; }
  .label--conditioner .brand-sub { top: 221px; font-size: 12px; }
  .label--bodywash .brand-name { top: 168px; font-size: 34px; }
  .label--bodywash .brand-sub { top: 210px; font-size: 12px; }
  .label--salt .brand-name { top: 93px; font-size: 20px; color: var(--swatch); }
  .label--salt .brand-sub { top: 113px; font-size: 8px; color: var(--swatch); }

  .label--conditioner .product-name { top: 299px; font-size: 28px; }
  .label--bodywash .product-name { top: 277px; font-size: 28px; }
  .label--salt .product-name { top: 161px; font-size: 19px; }

  .claim { line-height: 1.25; }
  .label--conditioner .claim { top: 370px; font-size: 22px; }
  .label--bodywash .claim { top: 346px; font-size: 16px; }
  .label--salt .claim { top: 201px; font-size: 16px; }

  .label--conditioner .hair-type {
    top: 457px; left: 96px; right: auto; width: 85px; height: 97px;
    background: var(--swatch); color: #fff;
    font-size: 12px; line-height: 1.25; padding-top: 6px;
  }

  .net-weight { font-size: 11px; }
  .label--conditioner .net-weight { top: 570px; }
  .label--bodywash .net-weight { top: 631px; }
  .label--salt .net-weight { top: 297px; }
</style>
</head>
<body>

<section class="label label--conditioner">
  <div class="leaf-area" role="img" aria-label="Soft white palm leaf illustration"></div>
  <div class="brand-mark"></div>
  <p class="brand-name">KELVARA</p>
  <p class="brand-sub">LUXURY LODGE</p>
  <h2 class="product-name">CONDITIONER</h2>
  <p class="claim">100%<br>PURE &amp; ORGANIC</p>
  <p class="hair-type">HAIR TYPE:<br>STRAIGHT<br>WAVY<br>CURLY<br>COILY<br>COARSE</p>
  <p class="net-weight">16 oz (473g)</p>
</section>

<section class="label label--bodywash">
  <div class="leaf-area" role="img" aria-label="Soft white palm leaf illustration"></div>
  <div class="brand-mark"></div>
  <p class="brand-name">KELVARA</p>
  <p class="brand-sub">LUXURY LODGE</p>
  <h2 class="product-name">BODY WASH</h2>
  <p class="claim">100%<br>PURE &amp; ORGANIC</p>
  <p class="net-weight">16 oz (473g)</p>
</section>

<section class="label label--salt">
  <div class="brand-mark"></div>
  <p class="brand-name">KELVARA</p>
  <p class="brand-sub">LUXURY LODGE</p>
  <h2 class="product-name">BLUE SEA SALT</h2>
  <p class="claim">100%<br>PURE &amp; ORGANIC</p>
  <p class="net-weight">16 oz (473g)</p>
</section>

</body>
</html>
```